Business Cards for a Junk Removal Company

Hello,
We are looking to have business cards designed that are simple, bold, easy to read, and right to the point. Please see the attachments for our logo files. We want the card to be yellow on both sides ( Color code Yellow: #FFE01B). The logo text font is (Rockstar Extra Bold) and this is also in the files attached. Please make the text black for the logo. On the back side of the card, you can use white and black for text. Thank you in advance for your hard work!

Front of card-
Harbor Haul Away (logo)
Back of card-
Harbor Haul Away
Donate - Recycle - Dispose
555-271-8093
www.harborhaulaway.example
info@harborhaulaway.example

Industry/Entity Type

Junk removal

Contact Information for Business Card

FRONT OF CARD- Harbor Haul Away (logo) BACK OF CARD- Harbor Haul Away Donate - Recycle - Dispose 555-271-8093 www.harborhaulaway.example info@harborhaulaway.example

Font styles to use
Other font styles liked:
• Rockstar Extra Bold

Colors
FFF300
FFF600
FEFA6F
FFFEC7
FFFEE8

Requirements
Must have
• Must have color code Yellow: #FFE01B for the background of front and back of the card

```html
<!DOCTYPE html>
<html lang="en">
<head>
<meta charset="utf-8">
<title>Harbor Haul Away — Business Cards</title>
<link rel="stylesheet" href="https://fonts.googleapis.com/css2?family=Barlow+Condensed:wght@600;800&display=swap">
<style>
  :root {
    --yellow: #FFE01B;
    --black: #000000;
    --white: #FFFFFF;
    --backdrop: #D3D4D6;
  }
  * { margin: 0; padding: 0; box-sizing: border-box; }
  html, body {
    width: 900px; height: 1200px; overflow: hidden;
    background: var(--backdrop);
    font-family: "Barlow Condensed", "Arial Narrow", sans-serif;
  }
  .card {
    position: absolute;
    left: 121px;
    width: 657px;
    height: 375px;
    background: var(--yellow);
    overflow: hidden;
  }
  .card--front { top: 204px; }
  .card--back { top: 621px; }

  .brand-name {
    position: absolute;
    color: var(--black);
    font-weight: 800;
    text-transform: uppercase;
    text-align: center;
    white-space: nowrap;
    line-height: 1;
  }
  .card--front .brand-name {
    left: 0; right: 0; top: 154px;
    font-size: 66px;
  }
  .card--back .brand-name {
    left: 0; width: 327px; top: 166px;
    font-size: 40px;
  }

  .tagline {
    position: absolute;
    left: 0; right: 0; top: 318px;
    text-align: center;
    font-weight: 800;
    font-size: 28px;
    letter-spacing: 0.03em;
    color: var(--black);
  }

  .contact-panel {
    position: absolute;
    left: 327px; top: 0;
    width: 330px; height: 100%;
    background: var(--black);
  }
  .contact-panel__name {
    position: absolute;
    left: 30px; top: 117px;
    font-weight: 800;
    font-size: 25px;
    letter-spacing: 0.01em;
    color: var(--yellow);
    text-transform: uppercase;
  }
  .contact-panel__role {
    position: absolute;
    left: 30px; top: 148px;
    font-weight: 600;
    font-size: 17px;
    letter-spacing: 0.03em;
    color: var(--white);
  }
  .contact-panel__rule {
    position: absolute;
    left: 30px; right: 0; top: 176px;
    height: 1px;
    background: var(--yellow);
  }
  .contact-list {
    position: absolute;
    left: 30px; top: 186px;
    list-style: none;
  }
  .contact-list__item {
    display: flex;
    align-items: center;
    height: 24.5px;
    color: var(--white);
    font-weight: 600;
    font-size: 17px;
    letter-spacing: 0.04em;
  }
  .contact-list__item--phone { letter-spacing: 0.18em; }
  .contact-list__icon {
    width: 12px; height: 12px;
    margin-right: 12px;
    flex: none;
  }
</style>
</head>
<body>

  <section class="card card--front" aria-label="Card front">
    <p class="brand-name">Harbor Haul Away</p>
    <p class="tagline">DONATE - RECYCLE - DISPOSE</p>
  </section>

  <section class="card card--back" aria-label="Card back">
    <p class="brand-name">Harbor Haul Away</p>

    <div class="contact-panel">
      <h1 class="contact-panel__name">Daniel Marsh</h1>
      <p class="contact-panel__role">Owner</p>
      <div class="contact-panel__rule"></div>

      <ul class="contact-list">
        <li class="contact-list__item contact-list__item--phone">
          <svg class="contact-list__icon" viewBox="0 0 24 24" aria-hidden="true">
            <path fill="#FFE01B" d="M6.6 10.8a15.1 15.1 0 0 0 6.6 6.6l2.2-2.2c.3-.3.7-.4 1-.2 1.1.4 2.3.6 3.6.6.6 0 1 .4 1 1V20c0 .6-.4 1-1 1A17 17 0 0 1 3 4c0-.6.4-1 1-1h3.5c.6 0 1 .4 1 1 0 1.3.2 2.5.6 3.6.1.3 0 .7-.2 1z"/>
          </svg>
          555-271-8093
        </li>
        <li class="contact-list__item">
          <svg class="contact-list__icon" viewBox="0 0 24 24" aria-hidden="true">
            <rect x="2" y="5" width="20" height="14" fill="#FFE01B"/>
            <path d="M2 5l10 8 10-8M2 19l7-7M22 19l-7-7" stroke="#000" stroke-width="1.6" fill="none"/>
          </svg>
          info@harborhaulaway.example
        </li>
        <li class="contact-list__item">
          <svg class="contact-list__icon" viewBox="0 0 24 24" aria-hidden="true">
            <g fill="none" stroke="#FFE01B" stroke-width="2">
              <circle cx="12" cy="12" r="9.5"/>
              <ellipse cx="12" cy="12" rx="4" ry="9.5"/>
              <path d="M2.5 12h19M4 7h16M4 17h16"/>
            </g>
          </svg>
          www.harborhaulaway.example
        </li>
      </ul>
    </div>
  </section>

</body>
</html>
```